Dental office stationary (letterhead, envelopes), business cards, presentation folders

Nothing too dental outside of the logo. I will need all stationary, presentation folders, business cards. Would prefer to stay in the colors of the logo

Gordon Pellham, DDS
Brightwell Dental Implant Center
772-555-0187
info@brightwelldental-example.com
3871 NW Corbin Rd Unit B
Palmview, FL 30000

Also need appointment date and time
And cancellation policy
I want it to say “kindly ask for
A 48hr cancellation policy to avoid incurring a cancellation fee”

Industry/Entity Type

Dental

Colors
0054AA
0677BA
7BADD7
CADEEF
E8F1F8

Requirements
Must have
• Name of your office, name of doctor, address, phone number
Should not have
• Too much tooth/dental. Only the tooth in logo

```html
<!DOCTYPE html>
<html lang="en">
<head>
<meta charset="utf-8">
<title>Brightwell Dental Implant Center – Stationery Set</title>
<link href="https://fonts.googleapis.com/css2?family=Lato:wght@400;700&display=swap" rel="stylesheet">
<style>
  :root{
    --navy:#0054AA;
    --blue:#0677BA;
    --sky:#7BADD7;
    --mist:#CADEEF;
    --ice:#E8F1F8;
    --paper:#F7F6F8;
    --white:#FFFFFF;
    --ink:#333A44;
    --stage:#3B3C3E;
    --brand-blue:linear-gradient(135deg,#2E9BE2 0%,#1A82D0 55%,#0E6CBC 100%);
  }
  *{box-sizing:border-box;margin:0;padding:0}
  html,body{width:1200px;height:292px;overflow:hidden}
  body{background:var(--stage);font-family:"Lato",Arial,sans-serif;color:var(--ink);position:relative}
  .piece{position:absolute;overflow:hidden;border-radius:3px}
  .wordmark{font-family:"Lato",Arial,sans-serif;font-weight:400;color:var(--blue);letter-spacing:.5px;white-space:nowrap;display:flex;align-items:center;gap:3px}
  .wordmark .dot{display:inline-block;border-radius:50%;background:currentColor}
  .wordmark.on-blue{color:var(--white)}
  .contact{font-size:3.3px;line-height:4.3px;color:var(--ink);white-space:nowrap}
  .contact .row{display:flex;align-items:center;gap:2px}
  .contact svg{width:3px;height:3px;fill:var(--blue);flex:none}
  .contact.on-blue{color:var(--white)}
  .contact.on-blue svg{fill:var(--white)}
  .faint-disc{position:absolute;border-radius:50%;background:var(--mist);opacity:.35}

  /* business card front */
  .card-front{left:25px;top:26px;width:125px;height:71px;background:var(--white)}
  .card-front .wordmark{position:absolute;left:11px;top:30px;font-size:8px}
  .card-front .wordmark .dot{width:4px;height:4px}
  .card-front .divider{position:absolute;left:62px;top:20px;width:.5px;height:36px;background:var(--sky)}
  .card-front .doctor{position:absolute;left:66px;top:20px}
  .card-front .contact{font-size:2.8px;line-height:3.8px}
  .card-front .contact svg{width:2.6px;height:2.6px}
  .doctor .name{font-size:4.6px;font-weight:700;color:var(--blue);letter-spacing:.2px;white-space:nowrap}
  .doctor .title{font-size:2.8px;color:var(--blue);margin-bottom:3px}

  /* business card back */
  .card-back{left:22px;top:110px;width:128px;height:73px;background:radial-gradient(ellipse at 55% 45%,#3AA6EA 0%,#1C85D2 60%,#0F6EBE 100%)}
  .card-back .wordmark{position:absolute;left:50%;top:50%;transform:translate(-50%,-50%);font-size:11px}
  .card-back .wordmark .dot{width:5px;height:5px}

  /* appointment card */
  .appt{left:22px;top:199px;width:128px;height:73px;background:var(--white)}
  .appt h3{font-size:5px;font-weight:700;color:var(--blue);text-align:center;margin-top:8px;letter-spacing:.1px}
  .appt .lines{margin:4px 7px 0}
  .appt .line{display:flex;align-items:flex-end;font-size:3.6px;color:var(--blue);height:8px;white-space:nowrap}
  .appt .fill{flex:1;border-bottom:.5px dotted var(--sky);margin:0 1px 1px}
  .appt .ampm{font-size:2.6px;margin-left:1px}
  .appt .bar{position:absolute;left:0;right:0;top:56px;height:5px;background:var(--blue);color:var(--white);font-size:3.3px;letter-spacing:.7px;text-align:center;line-height:5px;white-space:nowrap}
  .appt .policy{position:absolute;left:0;right:0;top:64px;font-size:2.8px;text-align:center;color:var(--ink);white-space:nowrap}

  /* letterhead */
  .letter{left:170px;top:25px;width:175px;height:247px;background:var(--paper);border-radius:1px}
  .letter .wordmark{position:absolute;left:17px;top:19px;font-size:5.5px}
  .letter .wordmark .dot{width:2.5px;height:2.5px}
  .letter .contact{position:absolute;left:120px;top:11px;font-size:2.6px;line-height:3.6px}
  .letter .contact svg{width:2.3px;height:2.3px}
  .letter .faint-disc{left:45px;top:112px;width:85px;height:85px}
  .letter .salute{position:absolute;left:17px;top:60px;font-size:4.6px}
  .letter .body{position:absolute;left:17px;top:75px;width:142px;font-size:2.5px;line-height:4.2px;text-align:justify}
  .letter .body p{margin-bottom:4px}
  .letter .sign{position:absolute;left:17px;top:169px;font-size:2.6px}
  .letter .sign svg{display:block;margin:3px 0 2px}
  .letter .sign .who{font-size:3.6px}
  .letter .sign .role{font-size:2.6px;color:#777}

  /* envelope back */
  .env-back{left:367px;top:53px;width:196px;height:89px;background:var(--paper);border-radius:1px}
  .env-back svg.flap{position:absolute;left:0;top:0}
  .env-back .wordmark{position:absolute;left:50%;top:18px;transform:translateX(-50%);font-size:8px}
  .env-back .wordmark .dot{width:3.5px;height:3.5px}

  /* envelope front */
  .env-front{left:366px;top:162px;width:197px;height:89px;background:var(--paper);border-radius:1px}
  .env-front .wordmark{position:absolute;left:12px;top:17px;font-size:6px}
  .env-front .wordmark .dot{width:2.8px;height:2.8px}
  .env-front .faint-disc{left:106px;top:8px;width:80px;height:80px}
  .env-front .contact{position:absolute;left:12px;top:57px;font-size:2.8px;line-height:3.7px}

  /* folder front */
  .folder-front{left:580px;top:61px;width:292px;height:183px;background:var(--white);border-radius:0}
  .folder-front .cover{position:absolute;left:0;top:0;width:146px;height:100%;background:var(--brand-blue)}
  .folder-front .cover .faint-disc{left:32px;top:20px;width:80px;height:80px;background:var(--white);opacity:.12}
  .folder-front .cover .contact{position:absolute;left:12px;top:154px;font-size:3.3px;line-height:4.3px}
  .folder-front .cover .web{position:absolute;left:92px;top:168px;font-size:3.3px;color:var(--white);white-space:nowrap}
  .folder-front .wordmark{position:absolute;left:219px;top:92px;transform:translate(-50%,-50%);font-size:13px}
  .folder-front .wordmark .dot{width:6px;height:6px}

  /* folder open */
  .folder-open{left:883px;top:62px;width:292px;height:184px;background:linear-gradient(90deg,#FFFFFF 0%,#F3F3F4 48%,#E4E4E6 50%,#F6F6F7 52%,#FFFFFF 100%);border-radius:0}
  .folder-open svg.pockets{position:absolute;left:0;top:0}
  .folder-open .wordmark{position:absolute;top:141px;transform:translate(-50%,-50%);font-size:11px}
  .folder-open .wordmark .dot{width:5px;height:5px}
  .folder-open .left{left:69px}
  .folder-open .right{left:227px}
</style>
</head>
<body>

<!-- Business card, front -->
<section class="piece card-front" aria-label="Business card front">
  <div class="wordmark"><span class="dot"></span>Brightwell</div>
  <div class="divider"></div>
  <div class="doctor">
    <div class="name">GORDON PELLHAM</div>
    <div class="title">DDS</div>
    <div class="contact">
      <div>3871 NW Corbin Rd Unit B</div>
      <div style="margin-bottom:2px">Palmview, FL 30000</div>
      <div class="row"><svg viewBox="0 0 10 10"><path d="M2 1l2 0 1 2.5-1.2 1a6 6 0 0 0 2.7 2.7l1-1.2L10 7v2a1 1 0 0 1-1 1A9 9 0 0 1 0 1a1 1 0 0 1 1-1z"/></svg>772-555-0187</div>
      <div class="row"><svg viewBox="0 0 10 10"><path d="M0 2h10v6H0z"/></svg>info@brightwelldental-example.com</div>
      <div class="row"><svg viewBox="0 0 10 10"><circle cx="5" cy="5" r="5"/></svg>www.brightwelldental-example.com</div>
    </div>
  </div>
</section>

<!-- Business card, back -->
<section class="piece card-back" aria-label="Business card back">
  <div class="wordmark on-blue"><span class="dot"></span>Brightwell</div>
</section>

<!-- Appointment card -->
<section class="piece appt" aria-label="Appointment card">
  <h3>Next Appointment</h3>
  <div class="lines">
    <div class="line">Date :<span class="fill"></span>Time :<span class="fill"></span><span class="ampm">AM/PM</span></div>
    <div class="line">Date :<span class="fill"></span>Time :<span class="fill"></span><span class="ampm">AM/PM</span></div>
    <div class="line">Date :<span class="fill"></span>Time :<span class="fill"></span><span class="ampm">AM/PM</span></div>
    <div class="line">Date :<span class="fill"></span>Time :<span class="fill"></span><span class="ampm">AM/PM</span></div>
  </div>
  <div class="bar">www.brightwelldental-example.com</div>
  <p class="policy">kindly ask for A 48hr cancellation policy to avoid incurring a cancellation fee</p>
</section>

<!-- Letterhead -->
<section class="piece letter" aria-label="Letterhead">
  <div class="faint-disc"></div>
  <div class="wordmark"><span class="dot"></span>Brightwell</div>
  <div class="contact">
    <div>3871 NW Corbin Rd Unit B</div>
    <div style="margin-bottom:1px">Palmview, FL 30000</div>
    <div class="row"><svg viewBox="0 0 10 10"><path d="M2 1l2 0 1 2.5-1.2 1a6 6 0 0 0 2.7 2.7l1-1.2L10 7v2a1 1 0 0 1-1 1A9 9 0 0 1 0 1a1 1 0 0 1 1-1z"/></svg>772-555-0187</div>
    <div class="row"><svg viewBox="0 0 10 10"><path d="M0 2h10v6H0z"/></svg>info@brightwelldental-example.com</div>
    <div class="row"><svg viewBox="0 0 10 10"><circle cx="5" cy="5" r="5"/></svg>www.brightwelldental-example.com</div>
  </div>
  <p class="salute">Dear Mr. Carver,</p>
  <div class="body">
    <p>Thank you for choosing our practice for your implant care. This letter confirms the details of your upcoming consultation and outlines what you can expect during your first visit with our team. We will begin with a short conversation about your goals, followed by a careful review of your health history, a gentle exam and any images needed to plan your treatment with confidence and clarity.</p>
    <p>Please bring a list of current medications, any recent dental records and your insurance card. Our coordinators will review treatment options, timelines and financing with you in person, and will answer every question before any work begins. Most first visits last about one hour, so we suggest arriving ten minutes early to complete a brief welcome form at the front desk.</p>
    <p>If you have questions before your appointment, our front desk is happy to help by phone or email during regular office hours, Monday through Friday. Should you need to change your visit, we kindly ask for at least forty-eight hours of notice so that we can offer the time to another patient and avoid a cancellation fee on your account with our office.</p>
    <p>We look forward to meeting you and helping you achieve a healthy, confident smile. Our whole team is committed to making each step of your care comfortable, clear and well planned, from the very first visit to your final follow-up, and we are grateful for the trust you place in us and in our practice.</p>
  </div>
  <div class="sign">
    <div>Sincerely,</div>
    <svg width="26" height="8" viewBox="0 0 26 8"><path d="M1 5 C6 2,12 2,16 4 S12 8,14 5 S20 3,25 4" fill="none" stroke="#222" stroke-width=".5"/></svg>
    <div class="who">Daniel Reeve</div>
    <div class="role">CEO/ Founder</div>
  </div>
</section>

<!-- Envelope, back -->
<section class="piece env-back" aria-label="Envelope back">
  <svg class="flap" width="196" height="33" viewBox="0 0 196 33">
    <defs><linearGradient id="flapFill" x1="0" y1="0" x2="1" y2="1"><stop offset="0" stop-color="#2E9BE2"/><stop offset="1" stop-color="#0E6CBC"/></linearGradient></defs>
    <path d="M0 0H196L190 24Q188 33 178 33H18Q8 33 6 24Z" fill="url(#flapFill)"/>
  </svg>
  <div class="wordmark on-blue"><span class="dot"></span>Brightwell</div>
</section>

<!-- Envelope, front -->
<section class="piece env-front" aria-label="Envelope front">
  <div class="faint-disc"></div>
  <div class="wordmark"><span class="dot"></span>Brightwell</div>
  <div class="contact">
    <div>3871 NW Corbin Rd Unit B</div>
    <div style="margin-bottom:1px">Palmview, FL 30000</div>
    <div class="row"><svg viewBox="0 0 10 10"><path d="M2 1l2 0 1 2.5-1.2 1a6 6 0 0 0 2.7 2.7l1-1.2L10 7v2a1 1 0 0 1-1 1A9 9 0 0 1 0 1a1 1 0 0 1 1-1z"/></svg>772-555-0187</div>
    <div class="row"><svg viewBox="0 0 10 10"><path d="M0 2h10v6H0z"/></svg>info@brightwelldental-example.com</div>
    <div class="row"><svg viewBox="0 0 10 10"><circle cx="5" cy="5" r="5"/></svg>www.brightwelldental-example.com</div>
  </div>
</section>

<!-- Presentation folder, outside -->
<section class="piece folder-front" aria-label="Presentation folder outside">
  <div class="cover">
    <div class="faint-disc"></div>
    <div class="contact on-blue">
      <div>3871 NW Corbin Rd Unit B</div>
      <div style="margin-bottom:1px">Palmview, FL 30000</div>
      <div class="row"><svg viewBox="0 0 10 10"><path d="M2 1l2 0 1 2.5-1.2 1a6 6 0 0 0 2.7 2.7l1-1.2L10 7v2a1 1 0 0 1-1 1A9 9 0 0 1 0 1a1 1 0 0 1 1-1z"/></svg>772-555-0187</div>
      <div class="row"><svg viewBox="0 0 10 10"><path d="M0 2h10v6H0z"/></svg>info@brightwelldental-example.com</div>
    </div>
    <div class="web">www.brightwelldental-example.com</div>
  </div>
  <div class="wordmark"><span class="dot"></span>Brightwell</div>
</section>

<!-- Presentation folder, inside -->
<section class="piece folder-open" aria-label="Presentation folder inside">
  <svg class="pockets" width="292" height="184" viewBox="0 0 292 184">
    <defs><linearGradient id="pocketFill" x1="0" y1="0" x2="1" y2="1"><stop offset="0" stop-color="#2E9BE2"/><stop offset="1" stop-color="#0E6CBC"/></linearGradient></defs>
    <path d="M0 109H128Q136 109 137 118L146 184H0Z" fill="url(#pocketFill)"/>
    <path d="M292 109H164Q156 109 155 118L146 184H292Z" fill="url(#pocketFill)"/>
  </svg>
  <div class="wordmark on-blue left"><span class="dot"></span>Brightwell</div>
  <div class="wordmark on-blue right"><span class="dot"></span>Brightwell</div>
</section>

</body>
</html>
```